Luxury sell sheet flyer Design

We need two luxury/premium looking sales flyer - one for luxury and one for travel-

Please find flyers from last year (2015) attached. Please copy the pictures and the look and feel (and colors), and use the content form the 2016 documents.

These flyers will be used for corporate subscription sales and targetted at CMOs and Marketing heads. As such they should convey a very premium look and feel.

Please provide in format that we can make text edits in later.

Target Market(s)

USA, UK, Asia

Industry/Entity Type

Travel

Font styles to use
Serif

Requirements
Must have
• Good copyright free pictures, no clip art, that show a very premium look and feel for a corporate flyer
Nice to have
• clean feel, not cluttered
Should not have
• clip art

```html
<!DOCTYPE html>
<html lang="en">
<head>
<meta charset="utf-8">
<title>Semi-Annual Roundtables – Tri-fold Brochure</title>
<link rel="stylesheet" href="https://fonts.googleapis.com/css2?family=Exo+2:wght@400;500;600&family=Arimo:wght@400&display=swap">
<style>
  :root {
    --stage: #d9d9db;
    --panel: #3b3f4d;
    --panel-edge: #343846;
    --card: #2d313d;
    --ink: #e7e9ef;
    --ink-soft: #c7cbd6;
    --heading: #ffffff;
    --pill: #4b5062;
    --sky-top: #9cc3e2;
    --sky-low: #d7e6f0;
    --sea: #3d6d8a;
  }
  * { box-sizing: border-box; margin: 0; padding: 0; }
  html, body { width: 1200px; height: 761px; overflow: hidden; }
  body {
    background: var(--stage);
    font-family: "Arimo", Arial, sans-serif;
    color: var(--ink);
  }
  .brochure {
    position: absolute;
    left: 50px; top: 70px;
    width: 1100px; height: 620px;
    display: flex;
    background: var(--panel);
    border-radius: 4px;
    box-shadow: 0 18px 40px rgba(0,0,0,.25);
  }
  .panel {
    position: relative;
    width: 366.6px; height: 100%;
    padding: 30px 26px;
  }
  .panel + .panel { border-left: 1px solid var(--panel-edge); }
  .panel__title {
    font-family: "Exo 2", sans-serif;
    font-weight: 500;
    color: var(--heading);
    font-size: 28px;
    line-height: 1.02;
    text-transform: uppercase;
    letter-spacing: .5px;
  }
  .panel__title--soft {
    text-transform: none;
    color: var(--ink-soft);
    font-weight: 400;
    font-size: 24px;
    line-height: 1.1;
  }
  .tag {
    display: inline-block;
    margin-top: 8px;
    padding: 3px 8px;
    background: var(--pill);
    border-radius: 2px;
    font-size: 10px;
    color: var(--ink-soft);
  }
  .copy {
    margin-top: 16px;
    font-size: 12.5px;
    line-height: 1.32;
    text-align: justify;
    hyphens: auto;
  }
  .copy p + p { margin-top: 14px; }
  .hero {
    position: absolute;
    left: 14px; top: 380px;
    width: 705px; height: 196px;
    border-radius: 14px;
    background: linear-gradient(180deg, var(--sky-top) 0%, var(--sky-low) 55%, var(--sea) 100%);
  }
  .card {
    position: absolute;
    background: var(--card);
    border-radius: 10px;
    padding: 16px 14px;
    font-family: "Exo 2", sans-serif;
    font-size: 12.5px;
    line-height: 1.25;
    text-align: center;
    color: var(--ink);
    display: flex; align-items: center; justify-content: center;
  }
  .chip {
    position: absolute;
    width: 36px; height: 30px;
    background: var(--card);
    border-radius: 6px;
  }
  .photo {
    position: absolute;
    border-radius: 10px;
    border: 4px solid var(--card);
  }
  .photo--field { background: linear-gradient(180deg, #8fb7c9 0%, #c9a43a 60%, #8a6a1e 100%); }
  .photo--luggage { background: linear-gradient(160deg, #bfe0ee 0%, #5e9fbd 60%, #2c3b48 100%); }
  .photo--glassware { background: linear-gradient(160deg, #b7b2de 0%, #8a86c6 45%, #e0c39a 100%); }
</style>
</head>
<body>
  <main class="brochure">
    <section class="panel panel--intro">
      <h1 class="panel__title">Semi-Annual<br>Roundtables</h1>
      <span class="tag">with Senior Executives</span>
      <div class="copy">
        <p>Duis id mattis nisi. Quisque varius, lorem a biben dum vehicula, nulla leo consequat urna, vel inter dum dolor urna sed mi. Sed quis port titor magna, non cursus odio. Vivamus risus orci, tempus id ul lamcorper tincidunt, gravida eget ligula. Integer venenatis rhoncus tortor, ut venenatis elit tempus vitae.</p>
        <p>Donec sit amet facilisis ante. Maecenas mo lestie mollis odio at imperdiet. Curabitur sol licitudin in neque id tempor. Morbi bibendum purus et lacus rutrum, feugiat convallis odio cursus. Proin pre tium hendrerit vulputate. Sed velit lorem, aliquet nec rutrum eget, hen drerit a felis. Integer viverra arcu eu nulla dictum tempor.</p>
      </div>
    </section>

    <section class="panel panel--insights">
      <h2 class="panel__title panel__title--soft">Affluent Insights<br>Prestige</h2>
      <div class="copy">
        <p>Donec semper enim sem, ut rutrum tortor condi mentum elementum. Phasellus ultrices nulla in in terdum fringilla. Nunc adipiscing ac cumsan lectus, quis bibendum enim accum san ut. Vestibulum vestibulum eros eu eges tas condimentum. Aliquam a mattis lacus, et suscipit dui. Etiam ac justo vitae neque ve hicula viverra.</p>
        <p>Pellentesque ac p osuere quam. Praesent congue, sem id blandit lacinia, augue nunc dictum nulla, a fermentum nibh nisi at massa. Nulla dictum tortor est, vel ullamco rper purus ultricies non. Quisque non vulputate turpis, eu ornare nibh. Aliquam vitae leo eget mauris semper malesuada nec a nisl. Nulla posuere lorem quis urna aliquam fermentum.</p>
      </div>
    </section>

    <div class="hero" role="img" aria-label="Travel photo: smiling couple in sun hats with a map, world landmarks and an airliner in a blue sky"></div>

    <section class="panel panel--highlights">
      <div class="card" style="left:22px;top:28px;width:200px;height:130px;">Cras pellentesque dui egestas lectus ultrices ornare. Quisque commodo non massaleo sed porhulita. Praesent sed uina id tur.</div>
      <div class="photo photo--field" style="left:236px;top:18px;width:112px;height:150px;" role="img" aria-label="Photo of a woman in a sunflower field with arms spread"></div>

      <div class="chip" style="left:150px;top:180px;"></div>
      <div class="photo photo--luggage" style="left:30px;top:196px;width:122px;height:232px;" role="img" aria-label="Photo of a vintage suitcase covered in travel stickers"></div>
      <div class="card" style="left:166px;top:226px;width:180px;height:150px;">Cras pellentesque dui egestas lectus ultrices ornare. Quisque commodo non massaleo sed porhulita. Praesent sed uina id tur.</div>

      <div class="chip" style="left:196px;top:392px;"></div>
      <div class="photo photo--glassware" style="left:244px;top:380px;width:112px;height:215px;" role="img" aria-label="Photo of crystal wine glasses on a set dining table"></div>
      <div class="card" style="left:66px;top:442px;width:168px;height:150px;">Cras pellentesque dui egestas lectus ultrices ornare. Quisque commodo non massaleo sed porhulita. Praesent sed uina id tur.</div>
    </section>
  </main>
</body>
</html>
```